Book cover for the book The Copper Lantern Beneath Harrow Lake

This is a 6x9 paperback book titled The Copper Lantern Beneath Harrow Lake: Field Notes on Tidal Rhythms from Sailors and Keepers Along the Northern Coast. It will be a cover full of love, reunion, and warmth. No ghosts, cemeteries, and so on. I'm open to any creative design. Might include someone rising in spirit from a sick bed to the welcoming arms of loved ones. Or someone being greeted by family in a scene of enchanting beauty that is the life after this life. The world of the life after this life is just like earth, except more beautiful, with colors we can't imagine, large flowers, opulent buildings, and people all young wearing robes of varying colors. No religious symbols. No sun, moon, or stars.

Font styles to use
Serif

Requirements
Should not have
• Cemeteries, ghosts, anything ghoulish and spooky

```html
<!DOCTYPE html>
<html lang="en">
<head>
<meta charset="utf-8">
<title>The Copper Lantern Beneath Harrow Lake — Cover</title>
<link rel="stylesheet" href="https://fonts.googleapis.com/css2?family=Outfit:wght@500;600&family=Red+Hat+Display:ital,wght@1,300&family=Great+Vibes&display=swap">
<style>
  :root {
    --page-bg: #e6eaec;
    --cover-bg: #1e1e1e;
    --title-red: #f0141a;
    --title-white: #ffffff;
    --body-white: #f2f2f2;
    --bird-red: #e3161c;
    --bird-grey: #8a8a8a;
  }
  * { margin: 0; padding: 0; box-sizing: border-box; }
  html, body {
    width: 1200px;
    height: 675px;
    overflow: hidden;
    background: var(--page-bg);
  }
  .stage {
    width: 1200px;
    height: 675px;
    display: flex;
    justify-content: center;
    align-items: center;
  }
  .cover {
    position: relative;
    width: 450px;
    height: 675px;
    background: var(--cover-bg);
    color: var(--title-white);
    text-align: center;
    overflow: hidden;
  }
  .title {
    position: absolute;
    top: 72px;
    left: 0;
    right: 0;
    font-family: "Outfit", sans-serif;
    font-weight: 600;
    line-height: 1;
  }
  .title__line { display: block; letter-spacing: -0.5px; }
  .title__line--red { color: var(--title-red); }
  .title__line--the { font-size: 40px; }
  .title__line--main { font-size: 40px; margin-top: 2px; }
  .title__line--white { color: var(--title-white); font-size: 34px; margin-top: 8px; }
  .title__script {
    display: block;
    font-family: "Great Vibes", cursive;
    font-weight: 400;
    font-size: 100px;
    line-height: 0.9;
    color: var(--title-white);
    margin-top: -4px;
  }
  .artwork {
    position: absolute;
    left: 25px;
    top: 322px;
    width: 400px;
    height: 150px;
  }
  .subtitle {
    position: absolute;
    top: 536px;
    left: 0;
    right: 0;
    font-family: "Red Hat Display", sans-serif;
    font-style: italic;
    font-weight: 300;
    font-size: 15.5px;
    line-height: 1.35;
    color: var(--body-white);
  }
  .author {
    position: absolute;
    top: 606px;
    left: 0;
    right: 0;
    font-family: "Outfit", sans-serif;
    font-weight: 600;
    font-size: 22px;
    color: var(--title-white);
  }
</style>
</head>
<body>
  <main class="stage">
    <section class="cover">
      <h1 class="title">
        <span class="title__line title__line--red title__line--the">THE</span>
        <span class="title__line title__line--red title__line--main">COPPER LANTERN</span>
        <span class="title__line title__line--white">BENEATH HARROW</span>
        <span class="title__script">Lake</span>
      </h1>

      <svg class="artwork" viewBox="0 0 400 150" role="img" aria-label="Illustration of red and grey origami birds flying upward across the cover">
        <defs>
          <radialGradient id="birdGlowRed" cx="50%" cy="50%" r="50%">
            <stop offset="0%" stop-color="var(--bird-red)" stop-opacity="0.55"/>
            <stop offset="100%" stop-color="var(--bird-red)" stop-opacity="0"/>
          </radialGradient>
          <radialGradient id="birdGlowGrey" cx="50%" cy="50%" r="50%">
            <stop offset="0%" stop-color="var(--bird-grey)" stop-opacity="0.35"/>
            <stop offset="100%" stop-color="var(--bird-grey)" stop-opacity="0"/>
          </radialGradient>
        </defs>
        <ellipse cx="40" cy="112" rx="50" ry="36" fill="url(#birdGlowRed)"/>
        <ellipse cx="108" cy="62" rx="48" ry="32" fill="url(#birdGlowGrey)"/>
        <ellipse cx="210" cy="55" rx="56" ry="42" fill="url(#birdGlowRed)"/>
        <ellipse cx="345" cy="30" rx="52" ry="30" fill="url(#birdGlowRed)"/>
      </svg>

      <p class="subtitle">Field Notes on Tidal Rhythms from Sailors<br>and Keepers Along the Northern Coast</p>
      <p class="author">Author name</p>
    </section>
  </main>
</body>
</html>
```